SnackHarbor!!! A Vending Machine Business Looking for an attractive website.

We are a vending machine business in Northern Michigan. We have changed our name and have rebranded our company. We would like an attractive website that shares who we are, what services we provide, the products we offer in our machines, along with a form businesses can fill out to see if they are a good fit for our company. I would like to have a Home Page, About SnackHarbor, Why Choose SnackHarbor?, Products & Services, Contact Us (With a Login Option), and a page with a questionnaire for thos interested in getting a FREE Vending Machine.

Target Market(s)

Businesses, Campgrounds, Schools, and many more in Northern Michigan

Industry/Entity Type

Vending Machines

Number of Pages Required

5+ page

Requirements
Must have
• An inviting and enticing Home Page. I want to get my potential clients engaged in our website.
Nice to have
• Possibly background photos from Northern Michigan
Should not have
• A corporate feel. I do not want a boring website.

```html
<!DOCTYPE html>
<html lang="en">
<head>
<meta charset="utf-8">
<title>SnackHarbor – Crave. Vend. Repeat.</title>
<link href="https://fonts.googleapis.com/css2?family=League+Spartan:wght@500;600;700;800&family=Outfit:wght@300;400;500;600&display=swap" rel="stylesheet">
<style>
:root{
  --navy:#1f2163;
  --navy-deep:#181a52;
  --green:#2e5b26;
  --green-bright:#3f7a2f;
  --ink:#111111;
  --text:#333333;
  --muted:#6b6f78;
  --panel:#eef1f6;
  --field:#f3f4f6;
  --line:#d9dce3;
  --white:#ffffff;
}
*{box-sizing:border-box;margin:0;padding:0}
html,body{width:1200px;height:4172px;overflow:hidden}
body{font-family:"Outfit",sans-serif;color:var(--text);background:var(--white);position:relative}
.section{position:absolute;left:0;width:1200px;overflow:hidden}
.abs{position:absolute}
.heading{font-family:"League Spartan",sans-serif;font-weight:700;color:var(--ink);letter-spacing:-.3px}
.eyebrow{font-family:"Outfit",sans-serif;font-size:14px;letter-spacing:3.5px;color:var(--green);text-transform:uppercase;font-weight:500}
.pill{display:inline-flex;align-items:center;justify-content:center;border-radius:20px;font-family:"League Spartan",sans-serif;font-weight:700;font-size:14px;color:var(--white);text-decoration:none}
.placeholder{background:linear-gradient(180deg,#f7f7f7,#e3e6e3);border-radius:6px}

/* hero */
.hero{top:0;height:625px;background:linear-gradient(180deg,#1c2b4b 0%,#22454a 45%,#2c5a2a 100%)}
.brand{font-family:"League Spartan",sans-serif;font-weight:800;color:var(--white);font-size:34px;display:flex;align-items:center;gap:10px}
.brand .dot{width:18px;height:18px;border-radius:50%;background:var(--white)}
.nav{top:26px;left:382px;display:flex;gap:34px}
.nav a{font-family:"Outfit",sans-serif;font-size:15px;color:var(--white);text-decoration:none;text-transform:uppercase}
.nav a.active{font-weight:600}
.login{left:992px;top:17px;width:107px;height:36px;background:var(--green);gap:6px}
.hero-title{left:100px;top:258px;font-size:54px;color:var(--white);font-weight:800}
.hero-sub{left:100px;top:316px;font-family:"Outfit",sans-serif;font-size:29px;color:var(--white);letter-spacing:1px}
.hero-btn{left:100px;top:376px;width:156px;height:37px;border:2px solid var(--white)}
.hero-machine{left:632px;top:121px;width:316px;height:438px;background:linear-gradient(160deg,#ffffff,#d8dcd6);border-radius:4px}
.dots{left:552px;top:579px;display:flex;gap:13px}
.dots span{width:14px;height:14px;border-radius:50%;border:2px solid var(--white)}
.dots span.on{background:var(--white)}

/* about */
.about{top:625px;height:541px;background:var(--white)}
.about-navy{left:100px;top:73px;width:152px;height:200px;background:var(--navy-deep)}
.about-green{left:431px;top:249px;width:154px;height:208px;background:var(--green)}
.about-photo{left:112px;top:86px;width:460px;height:358px;background:linear-gradient(90deg,#8b8f8a 0%,#c9cbc6 45%,#d63a33 78%,#b62a26 100%)}
.about-copy{left:628px;top:124px;width:472px}
.about-copy h2{font-size:35px;margin-top:6px}
.about-copy p{font-size:13.6px;line-height:26px;margin-top:14px;text-align:justify;color:#2c2c2c}
.btn-green{background:var(--green);width:155px;height:35px;margin-top:27px}

/* products */
.products{top:1166px;height:625px;background:var(--panel)}
.center{left:0;width:1200px;text-align:center}
.products h2,.why h2,.reviews h2{font-size:36px;margin-top:6px}
.lead{font-size:14px;line-height:26px;margin-top:10px;color:#2c2c2c}
.cards{left:100px;top:231px;display:flex;gap:26px}
.card{width:230px;height:322px;background:var(--white);border-radius:4px;padding:20px 20px 0}
.card .placeholder{width:150px;height:203px;margin:0 auto}
.card h3{font-family:"Outfit",sans-serif;font-weight:400;font-size:17px;line-height:21px;color:var(--ink);margin-top:24px}
.more{font-family:"League Spartan",sans-serif;font-weight:700;font-size:12.5px;color:var(--green);text-decoration:underline;display:inline-block;margin-top:6px}

/* why */
.why{top:1791px;height:654px;background:var(--white)}
.why-ring{left:421px;top:179px;width:358px;height:358px;border-radius:50%;background:#eceef2;border:5px solid #dcdfe5}
.why-machine{left:505px;top:217px;width:191px;height:250px;background:linear-gradient(160deg,#ffffff,#d8dcd6);border-radius:4px}
.icon{width:80px;height:80px;border-radius:50%;background:var(--navy);display:flex;align-items:center;justify-content:center}
.feature h3{font-family:"League Spartan",sans-serif;font-weight:700;font-size:15.5px;color:var(--ink);line-height:19px}
.feature p{font-size:11.8px;line-height:21px;margin-top:6px;color:#2c2c2c}
.feature.left{text-align:right}
.feature.left p{text-align:justify;text-align-last:right}
.feature b{color:var(--navy)}

/* reviews */
.reviews{top:2445px;height:469px;background:var(--panel)}
.review-row{left:99px;top:166px;display:flex;gap:24px}
.review{width:317px;height:227px;background:var(--white);border-radius:3px;text-align:center;padding:36px 22px 0}
.quote{font-family:"League Spartan",sans-serif;font-weight:800;font-size:44px;line-height:28px;color:var(--green);height:30px}
.review p{font-size:14px;line-height:22.6px;color:#333;margin-top:10px}
.review .who{font-family:"Outfit",sans-serif;font-weight:500;font-size:14.5px;color:var(--green);margin-top:10px}
.arrow{width:24px;height:40px}

/* contact */
.contact{top:2914px;height:551px;background:var(--white)}
.contact-ring{left:76px;top:46px;width:421px;height:424px;border-radius:50%;border:2px dashed #b9bcc2}
.contact-machine{left:105px;top:41px;width:381px;height:445px;background:linear-gradient(160deg,#ffffff,#d4d8d3);border-radius:4px}
.contact-copy{left:633px;top:82px;width:466px}
.contact-copy h2{font-size:35px;margin-top:6px}
.form-grid{display:grid;grid-template-columns:227px 226px;column-gap:13px;margin-top:12px}
.field label{display:block;font-size:10.5px;color:#444;height:13px}
.field .box{height:36px;background:var(--field);border:1px solid var(--line);margin-top:1px;margin-bottom:19px}
.field.full{grid-column:1 / 3}
.field.full .box{height:94px;margin-bottom:18px}
.submit{margin-left:309px;width:157px;height:37px;background:var(--green)}

/* signup */
.signup{top:3465px;height:366px;background:linear-gradient(180deg,#222c63 0%,#283f5a 50%,#2f5a2c 100%)}
.signup .eyebrow{color:var(--white)}
.signup h2{font-size:37px;line-height:42px;color:var(--white);margin-top:8px}
.signup p{font-size:14.5px;line-height:23px;color:var(--white);margin-top:10px}
.btn-navy{background:var(--navy-deep);width:156px;height:34px;margin-top:26px}

/* footer */
.footer{top:3831px;height:341px;background:var(--navy);color:var(--white)}
.footer .brand{font-size:40px}
.socials{left:148px;top:140px;display:flex;gap:9px}
.socials span{width:34px;height:34px;border-radius:50%;border:1.5px solid var(--white)}
.col h4{font-family:"League Spartan",sans-serif;font-weight:600;font-size:19px}
.col ul{list-style:none;margin-top:14px}
.col li{font-size:14px;line-height:33.5px}
.contact-list li{display:flex;gap:10px;line-height:20px;margin-bottom:17px}
.copyright{left:0;width:1200px;top:299px;text-align:center;font-size:13.5px}
</style>
</head>
<body>

<header class="section hero">
  <div class="abs brand" style="left:100px;top:20px"><span class="dot"></span>SnackHarbor</div>
  <nav class="abs nav">
    <a class="active" href="#">Home</a><a href="#">About SnackHarbor</a><a href="#">Products</a><a href="#">Services</a><a href="#">Contact Us</a>
  </nav>
  <a class="abs pill login" href="#">
    <svg width="15" height="15" viewBox="0 0 16 16"><circle cx="8" cy="8" r="8" fill="#fff"/><circle cx="8" cy="6" r="2.6" fill="#2e5b26"/><path d="M3.5 13a5 4 0 0 1 9 0" fill="#2e5b26"/></svg>LOGIN</a>
  <svg class="abs arrow" style="left:52px;top:296px" viewBox="0 0 24 40"><path d="M18 4 6 20l12 16" fill="none" stroke="#fff" stroke-width="2"/></svg>
  <svg class="abs arrow" style="left:1120px;top:296px" viewBox="0 0 24 40"><path d="M6 4l12 16L6 36" fill="none" stroke="#fff" stroke-width="2"/></svg>
  <h1 class="abs heading hero-title">SNACKHARBOR</h1>
  <div class="abs hero-sub">CRAVE. VEND. REPEAT.</div>
  <a class="abs pill hero-btn" href="#">GET STARTED »</a>
  <div class="abs hero-machine" role="img" aria-label="White branded snack vending machine stocked with snacks and drinks"></div>
  <div class="abs dots"><span></span><span class="on"></span><span></span><span></span></div>
</header>

<section class="section about">
  <div class="abs about-navy"></div>
  <div class="abs about-green"></div>
  <div class="abs about-photo" role="img" aria-label="Customer paying by card at a drinks vending machine"></div>
  <div class="abs about-copy">
    <div class="eyebrow">About Us</div>
    <h2 class="heading">WELCOME TO SNACKHARBOR</h2>
    <p>At SnackHarbor, we don't just vend snacks—we curate cravings. Our customized vending solutions bring flavor, convenience, &amp; community to Northern Michigan. Whether you're reaching for a mid-morning snack, a refreshing beverage, or a satisfying breakfast burrito, SnackHarbor delivers delight with every bite.</p>
    <a class="pill btn-green" href="#">LEARN MORE »</a>
  </div>
</section>

<section class="section products">
  <div class="abs center" style="top:72px">
    <div class="eyebrow">Our Product</div>
    <h2 class="heading">VENDING MACHINE</h2>
    <p class="lead">When it comes to healthy options, our machines can't be beat! We have a large selection of products<br>to choose from.Our machines are fully customized to suit the needs of each location.</p>
  </div>
  <div class="abs cards">
    <article class="card"><div class="placeholder" role="img" aria-label="Snack vending machine"></div><h3>Thirsty Vending<br>Machine</h3><a class="more" href="#">LEARN MORE »</a></article>
    <article class="card"><div class="placeholder" role="img" aria-label="Snack vending machine"></div><h3>CrunchVending<br>Machine</h3><a class="more" href="#">LEARN MORE »</a></article>
    <article class="card"><div class="placeholder" role="img" aria-label="Snack vending machine"></div><h3>Pleasures Vending<br>Machine</h3><a class="more" href="#">LEARN MORE »</a></article>
    <article class="card"><div class="placeholder" role="img" aria-label="Snack vending machine"></div><h3>Want Something Vending<br>Machine</h3><a class="more" href="#">LEARN MORE »</a></article>
  </div>
</section>

<section class="section why">
  <div class="abs center" style="top:69px">
    <div class="eyebrow">Why Us</div>
    <h2 class="heading">WHY CHOOSE SNACKHARBOR?</h2>
  </div>
  <div class="abs why-ring"></div>
  <div class="abs why-machine" role="img" aria-label="Branded snack vending machine"></div>

  <div class="abs icon" style="left:405px;top:199px"><svg width="38" height="38" viewBox="0 0 24 24" fill="none" stroke="#fff" stroke-width="1.4"><path d="M12 21s-7-6.5-7-12a7 7 0 0 1 14 0c0 5.5-7 12-7 12z"/><path d="M12 12.5l-2.6-2.4a1.6 1.6 0 0 1 2.6-1.8 1.6 1.6 0 0 1 2.6 1.8z"/></svg></div>
  <div class="abs icon" style="left:714px;top:199px"><svg width="38" height="38" viewBox="0 0 24 24" fill="none" stroke="#fff" stroke-width="1.4"><rect x="5" y="3" width="14" height="18"/><path d="M5 13h14M9 3v10M13 3v10M5 8h14M9 17h6"/></svg></div>
  <div class="abs icon" style="left:405px;top:417px"><svg width="38" height="38" viewBox="0 0 24 24" fill="none" stroke="#fff" stroke-width="1.4"><circle cx="12" cy="7" r="3.5"/><path d="M10.5 7l1.2 1.2 2-2.2"/><path d="M3 12l4 5h4M21 12l-4 5h-4M7 21v-4M17 21v-4"/></svg></div>
  <div class="abs icon" style="left:714px;top:417px"><svg width="38" height="38" viewBox="0 0 24 24" fill="none" stroke="#fff" stroke-width="1.4"><rect x="5" y="2" width="14" height="20" rx="1"/><path d="M8 5h6v10H8zM16 6h1M16 9h1M8 18h8M8 8h6M8 11h6"/></svg></div>

  <div class="abs feature left" style="left:97px;top:201px;width:292px">
    <h3>LOCAL LOVE</h3>
    <p>We celebrate the heart of Michigan by partnering with local legends. Say hello to Pinecrest Jerky and Lakeshore Chip Co.—our hometown heroes. Their flavors dance on your taste buds, and we're thrilled to bring them straight to your workplace.</p>
  </div>
  <div class="abs feature" style="left:808px;top:201px;width:292px">
    <h3>UNLEASH YOUR CRAVINGS</h3>
    <p>SnackHarbor isn't bound by corporate ties. We're the rebels of the vending world. Craving a bag of crispy, kettle-cooked chips? Done. Hankering for jerky that packs a punch? We've got you covered. Our machines are like treasure chests, waiting for you to unlock flavor magic.</p>
  </div>
  <div class="abs feature left" style="left:97px;top:418px;width:292px">
    <h3>QUALITY MEETS CONVENIENCE</h3>
    <p>Imagine this: You're mid-meeting, and your stomach growls. Fear not! SnackHarbor's machines offer top-notch snacks and beverages. It's like having a mini food festival at your fingertips. <b>Tap to Pay:</b> No fumbling for change! SnackHarbor accepts tap-to-pay options, credit cards, and even Orchard Pay and Glide Pay. Seamless snacking, guaranteed.</p>
  </div>
  <div class="abs feature" style="left:808px;top:418px;width:292px">
    <h3>PANDEMIC-PROOF &amp; RECESSION-<br>READY</h3>
    <p>Life throws curveballs, but SnackHarbor stands strong. Our vending machines are the unsung heroes of resilience. Rain or shine, they're there, serving up joy.</p>
  </div>
</section>

<section class="section reviews">
  <div class="abs center" style="top:74px">
    <div class="eyebrow">Testimonials</div>
    <h2 class="heading">OUR CLIENT REVIEWS</h2>
  </div>
  <svg class="abs arrow" style="left:61px;top:260px" viewBox="0 0 24 40"><path d="M17 8 7 20l10 12" fill="none" stroke="#1f2163" stroke-width="2"/></svg>
  <svg class="abs arrow" style="left:1113px;top:260px" viewBox="0 0 24 40"><path d="M7 8l10 12L7 32" fill="none" stroke="#1f2163" stroke-width="2"/></svg>
  <div class="abs review-row">
    <blockquote class="review"><div class="quote">”</div><p>Sed ut perspiciae omnis iste natus error sit voluptatem accuantium doloremque laudantium, totam aperiam, eaque ipsa quae ab illo inventore</p><div class="who">- MARA QUILL</div></blockquote>
    <blockquote class="review"><div class="quote">”</div><p>Sed ut perspiciae omnis iste natus error sit voluptatem accuantium doloremque laudantium, totam aperiam, eaque ipsa quae ab illo inventore</p><div class="who">- MARA QUILL</div></blockquote>
    <blockquote class="review"><div class="quote">”</div><p>Sed ut perspiciae omnis iste natus error sit voluptatem accuantium doloremque laudantium, totam aperiam, eaque ipsa quae ab illo inventore</p><div class="who">- MARA QUILL</div></blockquote>
  </div>
</section>

<section class="section contact">
  <div class="abs contact-ring"></div>
  <div class="abs contact-machine" role="img" aria-label="Large branded snack vending machine"></div>
  <div class="abs contact-copy">
    <div class="eyebrow">Contact Us</div>
    <h2 class="heading">BOOK A VENDING MACHINE</h2>
    <form class="form-grid">
      <div class="field"><label>Name</label><div class="box"></div></div>
      <div class="field"><label>Business Name</label><div class="box"></div></div>
      <div class="field"><label>Email</label><div class="box"></div></div>
      <div class="field"><label>Number</label><div class="box"></div></div>
      <div class="field full"><label>Your Message</label><div class="box"></div></div>
    </form>
    <a class="pill submit" href="#">SUBMIT »</a>
  </div>
</section>

<section class="section signup" role="img" aria-label="Background of vending machines in a softly lit hallway">
  <div class="abs center" style="top:68px">
    <div class="eyebrow">Sign Up</div>
    <h2 class="heading">READY TO EXPERIENCE<br>THE SNACKHARBOR DIFFERENCE</h2>
    <p>Sign up now and let's connect. Taste the future of snacking firsthand! Contact us today<br>and explore how our vending magic can elevate your space.</p>
    <a class="pill btn-navy" href="#">SUBMIT »</a>
  </div>
</section>

<footer class="section footer">
  <div class="abs brand" style="left:100px;top:62px"><span class="dot"></span>SnackHarbor</div>
  <div class="abs socials"><span></span><span></span><span></span><span></span></div>
  <div class="abs col" style="left:408px;top:40px">
    <h4>Quick Links</h4>
    <ul><li>Home</li><li>About SnackHarbor</li><li>Products</li><li>Services</li><li>Contact Us</li></ul>
  </div>
  <div class="abs col" style="left:635px;top:40px">
    <h4>Products</h4>
    <ul><li>Thirsty</li><li>Crunch</li><li>Guilty&nbsp; Pleasures</li><li>Want Something More</li></ul>
  </div>
  <div class="abs col" style="left:873px;top:38px">
    <h4>Contact Us</h4>
    <ul class="contact-list">
      <li><svg width="14" height="16" viewBox="0 0 24 24" fill="none" stroke="#fff" stroke-width="2.4"><path d="M12 22s-7-7-7-12a7 7 0 0 1 14 0c0 5-7 12-7 12z"/><circle cx="12" cy="10" r="2.5"/></svg><span>123 somewhere in<br>Location</span></li>
      <li><svg width="14" height="16" viewBox="0 0 24 24" fill="none" stroke="#fff" stroke-width="2.4"><path d="M5 3h4l2 5-3 2a11 11 0 0 0 6 6l2-3 5 2v4a2 2 0 0 1-2 2A18 18 0 0 1 3 5a2 2 0 0 1 2-2z"/></svg><span>+1 888 888 8888</span></li>
      <li><span style="width:14px"></span><span>info@SnackHarbor.com</span></li>
    </ul>
  </div>
  <div class="abs copyright">© 2024 SnackHarbor All Rights Reserved.</div>
</footer>

</body>
</html>
```